New Chartered Accounting Practice Needs Stationery Design

I need a new set of stationery including letterhead, business cards, envelopes and with compliments slips for a new Chartered Accounting Practice based in Melbourne, Victoria, Australia called "Martin K. Ashbury, Chartered Accountant".
I will be providing Taxation Services, Accounting Services, Self-Managed Superannuation Fund Consulting and general consulting advice to small and medium business enterprises. I would like to see designs that use the colour blue. The final design should communicate trust, technical expertise and security.
Target Market(s)
English speaking, Australians. Proprietors of small and medium businesses - aged 30-65. Fellow professionals - lawyers, investment consultants, other accountants. Retirees - aged 60 and over
Industry/Entity Type
Business
Look and feel

```html
<!DOCTYPE html>
<html lang="en">
<head>
<meta charset="utf-8">
<title>Martin K. Ashbury – With Compliments</title>
<link rel="stylesheet" href="https://fonts.googleapis.com/css2?family=Marcellus&family=Carlito&display=swap">
<style>
  :root {
    --brand-blue: #0433a0;
    --ink: #111111;
    --paper: #ffffff;
    --backdrop: #ffffff;
  }
  html, body {
    margin: 0;
    padding: 0;
    overflow: hidden;
    background: var(--backdrop);
  }
  .slip {
    position: relative;
    width: 1200px;
    height: 565px;
    background: var(--paper);
    overflow: hidden;
  }
  .slip__bands {
    position: absolute;
    inset: 0;
  }
  .brand {
    position: absolute;
    left: 702px;
    top: 58px;
    display: flex;
    align-items: center;
    gap: 14px;
    color: var(--brand-blue);
    font-family: "Marcellus", serif;
    font-weight: 400;
  }
  .brand__dot {
    width: 92px;
    height: 92px;
    border-radius: 50%;
    background: var(--brand-blue);
    flex: none;
  }
  .brand__name {
    margin: 0;
    font-size: 29px;
    line-height: 1.15;
    letter-spacing: 0.5px;
    text-transform: uppercase;
    font-weight: 400;
  }
  .brand__title {
    display: block;
    font-size: 24px;
    text-transform: none;
    letter-spacing: 0.3px;
    margin-top: 6px;
    padding-left: 22px;
  }
  .contact {
    position: absolute;
    left: 718px;
    top: 208px;
    margin: 0;
    padding: 0;
    list-style: none;
    font-family: "Carlito", sans-serif;
    font-size: 18px;
    color: var(--ink);
  }
  .contact__item {
    display: flex;
    align-items: center;
    height: 28.5px;
  }
  .contact__icon {
    width: 30px;
    height: 24px;
    margin-right: 8px;
    flex: none;
    fill: var(--ink);
  }
  .greeting {
    position: absolute;
    left: 106px;
    top: 474px;
    margin: 0;
    font-family: "Marcellus", serif;
    font-weight: 400;
    font-size: 38px;
    color: var(--paper);
    letter-spacing: 0.3px;
  }
</style>
</head>
<body>
<main class="slip">
  <svg class="slip__bands" width="1200" height="565" viewBox="0 0 1200 565" aria-hidden="true">
    <rect x="0" y="0" width="1200" height="12" fill="var(--brand-blue)"/>
    <path d="M114 0 H420 V4 Q420 42 382 42 H152 Q114 42 114 4 Z" fill="var(--brand-blue)"/>
    <rect x="0" y="448" width="1200" height="117" fill="var(--brand-blue)"/>
    <path d="M778 448 H1078 V444 Q1078 478 1044 478 H812 Q778 478 778 444 Z" fill="var(--paper)"/>
  </svg>

  <div class="brand">
    <span class="brand__dot" aria-hidden="true"></span>
    <p class="brand__name">Martin K. Ashbury<span class="brand__title">Chartered Accountant</span></p>
  </div>

  <ul class="contact">
    <li class="contact__item">
      <svg class="contact__icon" viewBox="0 0 30 24" aria-hidden="true">
        <path d="M15 1a8 8 0 0 0-8 8c0 6 8 14 8 14s8-8 8-14a8 8 0 0 0-8-8zm0 11a3.2 3.2 0 1 1 0-6.4 3.2 3.2 0 0 1 0 6.4z"/>
      </svg>
      Office : 18 Larkspur Street, Kew VIC 3101
    </li>
    <li class="contact__item">
      <svg class="contact__icon" viewBox="0 0 30 24" aria-hidden="true">
        <rect x="2" y="4" width="26" height="17" fill="none" stroke="#111" stroke-width="1.6"/>
        <rect x="21" y="7" width="4" height="4"/>
        <rect x="6" y="13" width="10" height="1.4"/>
        <rect x="6" y="16" width="12" height="1.4"/>
      </svg>
      Postal : PO Box 4417, Kew VIC 3101
    </li>
    <li class="contact__item">
      <svg class="contact__icon" viewBox="0 0 30 24" aria-hidden="true">
        <path d="M4 8c0-3 5-5 11-5s11 2 11 5v2h-5V8c0-1-3-1.5-6-1.5S9 7 9 8v2H4z"/>
        <path d="M8 12h14l3 10H5z"/>
        <circle cx="15" cy="16.5" r="2.6" fill="#fff"/>
      </svg>
      Phone: 0412 555 308
    </li>
    <li class="contact__item">
      <svg class="contact__icon" viewBox="0 0 30 24" aria-hidden="true">
        <rect x="8" y="1" width="14" height="7"/>
        <rect x="3" y="9" width="24" height="9" rx="2"/>
        <rect x="8" y="16" width="14" height="7" fill="#fff" stroke="#111" stroke-width="1.6"/>
      </svg>
      Fax: (03) 9555 0142
    </li>
    <li class="contact__item">
      <svg class="contact__icon" viewBox="0 0 30 24" aria-hidden="true">
        <path d="M4 5h22v2l-11 7L4 7z"/>
        <path d="M4 9.5l11 7 11-7V20H4z"/>
      </svg>
      martin.ashbury@example.com.au
    </li>
  </ul>

  <h1 class="greeting">With Compliments</h1>
</main>
</body>
</html>
```